Dalton Wire Supply, Inc. Business Card Design

We are an Electrical Distributor looking for a Modern, Professional Business Card design.

Target Market(s)

Residential Commercial Industrial

Industry/Entity Type

Electrical

Contact Information for Business Card

Dalton Wire Supply, Inc.
418 Birchwood Lane
Ashbury, TN 38412
910-555-2741
910-555-8196 Fax
daltonwire@pinemail.example

```html
<!DOCTYPE html>
<html lang="en">
<head>
<meta charset="utf-8">
<title>Dalton Wire Supply, Inc. – Business Card</title>
<link href="https://fonts.googleapis.com/css2?family=Montserrat:wght@400;500;700;800&display=swap" rel="stylesheet">
<style>
  :root {
    --backdrop: #e9e6e1;
    --card-dark: #0b0f16;
    --card-dark-2: #1a2230;
    --paper: #f7f7f7;
    --brand-blue: #1b9fdc;
    --ink-light: #d7dde5;
    --ink-muted: #aab3bf;
  }
  html, body {
    margin: 0;
    width: 1200px;
    height: 1022px;
    overflow: hidden;
    background: var(--backdrop);
  }
  .stage {
    position: relative;
    width: 1200px;
    height: 1022px;
  }
  .business-card {
    position: absolute;
    left: 100px;
    top: 225px;
    width: 1000px;
    height: 572px;
    border-radius: 16px;
    overflow: hidden;
    box-shadow: 0 10px 30px rgba(0,0,0,0.18);
  }
  .business-card svg { display: block; }
  .wordmark {
    font-family: "Montserrat", sans-serif;
    font-weight: 800;
    fill: var(--brand-blue);
    letter-spacing: 1px;
  }
  .holder-name {
    font-family: "Montserrat", sans-serif;
    font-weight: 700;
    fill: var(--brand-blue);
    font-size: 34px;
    letter-spacing: 1px;
  }
  .holder-title, .address-line, .contact-line {
    font-family: "Montserrat", sans-serif;
    fill: var(--ink-light);
  }
  .holder-title { font-size: 20px; font-weight: 500; letter-spacing: 2px; }
  .address-line { font-size: 20px; font-weight: 400; fill: var(--ink-muted); }
  .contact-line { font-size: 20px; font-weight: 400; }
  .contact-icon { fill: var(--brand-blue); }
</style>
</head>
<body>
<main class="stage">
  <section class="business-card" aria-label="Dalton Wire Supply business card">
    <svg width="1000" height="572" viewBox="0 0 1000 572" xmlns="http://www.w3.org/2000/svg">
      <defs>
        <linearGradient id="darkFill" x1="0" y1="0" x2="1" y2="1">
          <stop offset="0" stop-color="#1a2230"/>
          <stop offset="1" stop-color="#0b0f16"/>
        </linearGradient>
        <radialGradient id="cablePhoto" cx="0.5" cy="0.45" r="0.6">
          <stop offset="0" stop-color="#5a6a80"/>
          <stop offset="0.45" stop-color="#5b2a24"/>
          <stop offset="1" stop-color="#0b0f16" stop-opacity="0"/>
        </radialGradient>
      </defs>

      <rect class="card-base" width="1000" height="572" fill="url(#darkFill)"/>

      <rect class="cable-photo" x="330" y="220" width="340" height="352"
            fill="url(#cablePhoto)" role="img"
            aria-label="Photo of a stripped electrical cable with sparks"/>

      <path class="header-sweep" d="M0,0 H1000 V70 C760,175 380,300 0,330 Z" fill="var(--paper)"/>
      <path class="header-rule" d="M0,342 C380,312 760,187 1000,82" fill="none"
            stroke="var(--brand-blue)" stroke-width="8"/>

      <path class="footer-band" d="M0,572 V556 C420,540 760,470 1000,372 V572 Z" fill="var(--brand-blue)"/>

      <text class="wordmark" x="120" y="140" font-size="64">DALTON WIRE</text>
      <text class="wordmark" x="120" y="200" font-size="40">SUPPLY, INC.</text>
      <line class="wordmark-rule" x1="120" y1="222" x2="560" y2="222"
            stroke="var(--brand-blue)" stroke-width="2"/>

      <text class="holder-name" x="60" y="430">MARCUS HALE</text>
      <text class="holder-title" x="60" y="464">DIRECTOR</text>
      <text class="address-line" x="60" y="498">418 Birchwood Lane</text>
      <text class="address-line" x="60" y="526">Ashbury, TN 38412</text>

      <g class="contact-list">
        <path class="contact-icon" transform="translate(640,282)"
              d="M3,1 L7,0 L9,5 L6.5,7 C7.5,9.5 9.5,11.5 12,12.5 L14,10 L19,12 L18,16 C10,17 2,9 3,1 Z"/>
        <text class="contact-line" x="672" y="298">910-555-2741</text>

        <rect class="contact-icon" x="641" y="320" width="16" height="14" rx="2"/>
        <rect x="645" y="317" width="8" height="5" fill="var(--ink-light)"/>
        <text class="contact-line" x="672" y="334">910-555-8196</text>

        <rect x="640" y="356" width="18" height="13" rx="1.5" fill="none"
              stroke="var(--brand-blue)" stroke-width="2"/>
        <path d="M640,357 L649,364 L658,357" fill="none" stroke="var(--brand-blue)" stroke-width="2"/>
        <text class="contact-line" x="672" y="370">daltonwire@pinemail.example</text>
      </g>
    </svg>
  </section>
</main>
</body>
</html>
```